Kowalczyk Electric & Sons

We need a logo design and business card design for our electrical company. I would like to see designs with lightning and the bright green lettering.

Target Market(s)

Electrical contractor

Industry/Entity Type

Business

Contact Information for Business Card

204-558-WIRE(9473)
Marty Kowalczyk
www.kowalczykelectric.example
Owner

Colors
acd136

Requirements
Must have
• - New Construction
• - Commercial
• - Residential
• - Tenant improvements
• - Preventative Maintenance
• - Re-Models
• - Service Upgrades
• - Trouble Shooting
• - New Circuits
• All your electrical needs
• Lighting up Winnipeg and surrounding areas !

```html
<!DOCTYPE html>
<html lang="en">
<head>
<meta charset="utf-8">
<title>Kowalczyk Electric &amp; Sons — Business Card</title>
<link rel="stylesheet" href="https://fonts.googleapis.com/css2?family=Open+Sans:wght@400;600;700&display=swap">
<style>
  :root {
    --page-bg: #e9eae7;
    --card-light: #f4f5f2;
    --brand-green: #2fae2a;
    --panel-top: #66dd1a;
    --panel-bottom: #22a530;
    --panel-text: #ffffff;
  }
  * { margin: 0; padding: 0; box-sizing: border-box; }
  html, body {
    width: 1200px;
    height: 900px;
    overflow: hidden;
    background: var(--page-bg);
    font-family: "Open Sans", sans-serif;
  }
  .business-card {
    position: absolute;
    left: 150px;
    top: 172px;
    width: 900px;
    height: 556px;
    display: flex;
    box-shadow: 0 12px 40px rgba(0, 0, 0, 0.15);
  }
  .brand-side {
    width: 450px;
    height: 100%;
    background: var(--card-light);
    display: flex;
    flex-direction: column;
    align-items: center;
    justify-content: center;
    gap: 26px;
    padding-top: 10px;
  }
  .brand-ring {
    width: 150px;
    height: 150px;
    border: 6px solid var(--brand-green);
    border-radius: 50%;
  }
  .brand-name {
    color: var(--brand-green);
    font-weight: 600;
    font-size: 34px;
    line-height: 1.15;
    text-align: center;
  }
  .contact-side {
    width: 450px;
    height: 100%;
    background: linear-gradient(180deg, var(--panel-top) 0%, var(--panel-bottom) 100%);
    color: var(--panel-text);
    padding: 140px 0 0 51px;
  }
  .person-name {
    font-size: 29px;
    font-weight: 700;
    line-height: 1.2;
  }
  .person-title {
    font-size: 24px;
    font-weight: 400;
    line-height: 1.3;
  }
  .service-note {
    margin-top: 28px;
    font-size: 23px;
    line-height: 1.42;
  }
  .contact-list {
    list-style: none;
    margin-top: 26px;
    font-size: 22px;
    line-height: 1.45;
  }
  .contact-list li {
    display: flex;
    align-items: center;
    gap: 12px;
  }
  .contact-icon {
    width: 20px;
    height: 20px;
    flex: none;
    fill: var(--panel-text);
  }
</style>
</head>
<body>
  <div class="business-card">
    <section class="brand-side">
      <div class="brand-ring"></div>
      <div class="brand-name">Kowalczyk<br>Electric &amp; Sons</div>
    </section>
    <section class="contact-side">
      <div class="person-name">Marty Kowalczyk</div>
      <div class="person-title">Owner</div>
      <div class="service-note">All your electrical needs<br>Winnipeg and surrounding areas</div>
      <ul class="contact-list">
        <li>
          <svg class="contact-icon" viewBox="0 0 24 24" aria-hidden="true"><path d="M6.6 10.8c1.4 2.8 3.8 5.1 6.6 6.6l2.2-2.2c.3-.3.7-.4 1-.2 1.1.4 2.3.6 3.6.6.6 0 1 .4 1 1V20c0 .6-.4 1-1 1C10.6 21 3 13.4 3 4c0-.6.4-1 1-1h3.5c.6 0 1 .4 1 1 0 1.3.2 2.5.6 3.6.1.3 0 .7-.2 1L6.6 10.8z"/></svg>
          <span>204-558-WIRE(9473)</span>
        </li>
        <li>
          <svg class="contact-icon" viewBox="0 0 24 24" aria-hidden="true"><path d="M3 6h18v1.2l-9 6-9-6z"/><path d="M3 9l9 6 9-6v9H3z"/></svg>
          <span>info@kowalczykelectric.example</span>
        </li>
        <li>
          <svg class="contact-icon" viewBox="0 0 24 24" aria-hidden="true"><circle cx="12" cy="12" r="9"/><path d="M3.5 12h17M12 3.2c-3 3-3 14.6 0 17.6M12 3.2c3 3 3 14.6 0 17.6" fill="none" stroke="#2aa82e" stroke-width="1.5"/></svg>
          <span>www.kowalczykelectric.example</span>
        </li>
      </ul>
    </section>
  </div>
</body>
</html>
```